Business Card and Simple Logo Desgin

New Zealand based start up company "Brook Advisory LTD" requires business cards and simple logo design.

Card Content.

Brook Advisory LTD

Joanna Pritchard
CA, BMS (Hons)

j.pritchard@brookadvisory.co.nz
PH +64 21 574 160

Target Market(s)

Corporate Business in IT, Finance and accounting.

Industry/Entity Type

Business

```html
<!DOCTYPE html>
<html lang="en">
<head>
<meta charset="utf-8">
<title>Brook Advisory LTD – Business Card</title>
<link rel="stylesheet" href="https://fonts.googleapis.com/css2?family=EB+Garamond:wght@400&family=Federant&display=swap">
<style>
  :root {
    --card-light: #d6cfa8;
    --card-mid: #c4bc95;
    --card-shade: #a9a283;
    --ink: #1b1a16;
    --title-fill: #ddd6b2;
  }
  html, body {
    margin: 0;
    padding: 0;
    width: 1200px;
    height: 649px;
    overflow: hidden;
  }
  .card {
    position: relative;
    width: 1200px;
    height: 649px;
    overflow: hidden;
    color: var(--ink);
    font-family: "EB Garamond", Georgia, serif;
  }
  .card-backdrop {
    position: absolute;
    inset: 0;
    background:
      radial-gradient(ellipse 520px 420px at 880px 300px, var(--card-shade) 0%, rgba(169,162,131,0) 70%),
      radial-gradient(ellipse 420px 360px at 330px 330px, var(--card-mid) 0%, rgba(196,188,149,0) 75%),
      linear-gradient(135deg, var(--card-light) 0%, var(--card-mid) 55%, var(--card-light) 100%);
  }
  .company-name {
    position: absolute;
    left: 72px;
    top: 218px;
    margin: 0;
    font-family: "Federant", Georgia, serif;
    font-weight: 400;
    font-size: 44px;
    letter-spacing: 0.5px;
    color: var(--title-fill);
    -webkit-text-stroke: 1.2px var(--ink);
    white-space: nowrap;
  }
  .brand-mark {
    position: absolute;
    left: 710px;
    top: 95px;
    width: 340px;
    height: 340px;
  }
  .brand-mark-name {
    position: absolute;
    inset: 0;
    display: flex;
    align-items: center;
    justify-content: center;
    font-family: "EB Garamond", Georgia, serif;
    font-size: 34px;
    color: var(--ink);
  }
  .person {
    position: absolute;
    left: 68px;
    top: 398px;
    line-height: 1;
  }
  .person-name {
    margin: 0;
    font-size: 42px;
    font-weight: 400;
  }
  .person-credentials {
    margin: 2px 0 0;
    font-size: 31px;
  }
  .contact {
    position: absolute;
    left: 68px;
    top: 536px;
    margin: 0;
    font-size: 31px;
    line-height: 30px;
  }
  .contact span { display: block; }
</style>
</head>
<body>
  <div class="card">
    <div class="card-backdrop" role="img" aria-label="Soft blurred beige background texture"></div>

    <h1 class="company-name">Brook Advisory LTD</h1>

    <div class="brand-mark">
      <svg width="340" height="340" viewBox="0 0 340 340" aria-hidden="true">
        <circle cx="170" cy="170" r="165" fill="none" stroke="var(--ink)" stroke-width="2"/>
      </svg>
      <div class="brand-mark-name">Brook Advisory</div>
    </div>

    <div class="person">
      <p class="person-name">Joanna Pritchard</p>
      <p class="person-credentials">CA, BMS (Hons)</p>
    </div>

    <p class="contact">
      <span class="contact-email">j.pritchard@brookadvisory.co.nz</span>
      <span class="contact-phone">PH +64 21 574 160</span>
    </p>
  </div>
</body>
</html>
```